Banner Ad Design Project

We are a SEO company and need a banner design for our new service, the highlights being:

- Pay Per Performance SEO service
- Guaranteed Frobly page 1 ranking
- Only $197 per month (+ performance bonus)

Can be all on one static banner or made into an animated GIF - designers choice...

Site URL (not up yet) will be RankLoft.com (by Velbrin) - this is a spinoff site of our existing business, Velbrin LLC - logo attached and should be included on the banner.

Industry/Entity Type

Business

Requirements
Must have
• Banner delivered in multiple sizes:
- 200 x 200
- 250 x 250
- 300 x 250
- 336 x 280
- 468 x 60
- 728 x 90
- 120 x 600
- 160 x 600

```html
<!DOCTYPE html>
<html lang="en">
<head>
<meta charset="utf-8">
<title>RankLoft.com – Pay Per Performance SEO Banners</title>
<link rel="stylesheet" href="https://fonts.googleapis.com/css2?family=Arimo:wght@400;700&family=Archivo+Narrow:wght@400;500&display=swap">
<style>
  :root {
    --backdrop: #d8d5cf;
    --white: #ffffff;
    --navy: #1d3a8c;
    --accent-red: #e3122c;
    --lime: #8dc63f;
    --wordmark: #5f6468;
    --url-blue: #2b5fae;
    --button-top: #4a8fdc;
    --button-bottom: #1f58a6;
    --copy-panel: #e6e7ea;
    --photo-light: #efe3d6;
    --photo-mid: #d3b8a0;
    --photo-dark: #6b5a4e;
  }
  * { box-sizing: border-box; margin: 0; padding: 0; }
  html, body { width: 792px; height: 1200px; overflow: hidden; }
  body {
    position: relative;
    background: var(--backdrop);
    font-family: "Arimo", Arial, sans-serif;
    color: var(--navy);
  }
  .banner { position: absolute; background: var(--white); overflow: hidden; }

  /* brand wordmark: text only */
  .brand { position: absolute; display: flex; flex-direction: column; align-items: flex-start; }
  .brand-name { font-weight: 700; color: var(--wordmark); line-height: 1; }
  .brand-url { font-weight: 700; color: var(--url-blue); line-height: 1; }

  .photo { position: absolute; }

  .points { position: absolute; list-style: none; }
  .points li { position: relative; font-weight: 400; }
  .points li::before {
    content: ""; position: absolute; left: 0; border-radius: 50%; background: var(--navy);
  }
  .bonus { color: var(--accent-red); }

  .cta-band { position: absolute; background: var(--lime); }
  .cta {
    position: absolute; display: flex; align-items: center; justify-content: center; gap: 8px;
    border-radius: 6px;
    background: linear-gradient(var(--button-top), var(--button-bottom));
    box-shadow: 0 2px 3px rgba(0,0,0,.35);
    color: var(--white); font-family: "Arimo", Arial, sans-serif;
    letter-spacing: .3px; text-decoration: none;
  }

  /* square */
  .square { left: 152px; top: 485px; width: 300px; height: 298px; }
  .square .brand { left: 10px; top: 10px; }
  .square .brand-name { font-size: 31px; }
  .square .brand-url { font-size: 15px; margin: 6px 0 0 44px; }
  .square .photo { left: 155px; top: 0; width: 145px; height: 130px;
    background: radial-gradient(ellipse at 45% 45%, var(--photo-light) 0%, var(--photo-mid) 45%, var(--photo-dark) 100%); }
  .square .points { left: 6px; top: 132px; }
  .square .points li { font-size: 16.5px; padding-left: 14px; margin-bottom: 12px; white-space: nowrap; }
  .square .points li::before { width: 10px; height: 10px; top: 5px; }
  .square .points .bonus { font-size: 11px; }
  .square .cta-band { left: 0; top: 229px; width: 300px; height: 69px; }
  .square .cta { left: 70px; top: 243px; width: 161px; height: 42px; font-size: 16px; }

  /* skyscraper */
  .sky { left: 552px; top: 26px; width: 203px; height: 1012px; background: var(--copy-panel); }
  .sky .logo-strip { position: absolute; left: 0; top: 0; width: 203px; height: 105px; background: var(--white); }
  .sky .brand { left: 14px; top: 22px; }
  .sky .brand-name { font-size: 38px; }
  .sky .brand-url { font-size: 16px; margin: 8px 0 0 62px; }
  .sky .photo { left: 0; top: 105px; width: 203px; height: 430px;
    background: linear-gradient(180deg, var(--photo-mid) 0%, var(--photo-light) 35%, var(--photo-mid) 65%, var(--copy-panel) 100%); }
  .sky .points { left: 4px; top: 508px; width: 192px; font-family: "Archivo Narrow", "Arial Narrow", sans-serif; }
  .sky .points li { font-size: 29px; line-height: 37px; padding-left: 22px; margin-bottom: 16px; font-weight: 500; }
  .sky .points li::before { width: 17px; height: 17px; top: 10px; }
  .sky .points .bonus { display: block; font-size: 17px; line-height: 22px; font-weight: 400; }
  .sky .cta-band { left: 0; top: 904px; width: 203px; height: 108px; }
  .sky .cta { left: 11px; top: 934px; width: 182px; height: 48px; font-size: 18px; }

  /* leaderboard */
  .leader { left: 22px; top: 1062px; width: 731px; height: 89px; }
  .leader .brand { left: 12px; top: 18px; }
  .leader .brand-name { font-size: 31px; }
  .leader .brand-url { font-size: 15px; margin: 6px 0 0 44px; }
  .leader .points { left: 186px; top: 10px; }
  .leader .points li { font-size: 16.5px; padding-left: 16px; margin-bottom: 7px; white-space: nowrap; }
  .leader .points li::before { width: 10px; height: 10px; top: 5px; }
  .leader .points .bonus { font-size: 11px; }
  .leader .cta-band { left: 539px; top: 0; width: 192px; height: 89px; }
  .leader .cta { left: 552px; top: 26px; width: 171px; height: 42px; font-size: 16px; }
</style>
</head>
<body>

<section class="banner square">
  <div class="brand">
    <span class="brand-name">Velbrin</span>
    <span class="brand-url">RankLoft.com</span>
  </div>
  <div class="photo" role="img" aria-label="Photo of a smiling support agent wearing a headset"></div>
  <ul class="points">
    <li>Pay Per Performance SEO service</li>
    <li>Guaranteed Frobly page 1 ranking</li>
    <li>Only $197 per month <span class="bonus">(+performance bonus)</span></li>
  </ul>
  <div class="cta-band"></div>
  <a class="cta" href="#">LEARN MORE
    <svg width="12" height="10" viewBox="0 0 12 10"><path d="M1 1l4 4-4 4M6 1l4 4-4 4" fill="none" stroke="#fff" stroke-width="1.6"/></svg>
  </a>
</section>

<section class="banner sky">
  <div class="logo-strip"></div>
  <div class="brand">
    <span class="brand-name">Velbrin</span>
    <span class="brand-url">RankLoft.com</span>
  </div>
  <div class="photo" role="img" aria-label="Close-up photo of a smiling support agent with a headset microphone"></div>
  <ul class="points">
    <li>Pay Per Performance SEO service</li>
    <li>Guaranteed Frobly page 1 ranking</li>
    <li>Only $197 per month <span class="bonus">(+performance bonus)</span></li>
  </ul>
  <div class="cta-band"></div>
  <a class="cta" href="#">LEARN MORE
    <svg width="13" height="11" viewBox="0 0 12 10"><path d="M1 1l4 4-4 4M6 1l4 4-4 4" fill="none" stroke="#fff" stroke-width="1.6"/></svg>
  </a>
</section>

<section class="banner leader">
  <div class="brand">
    <span class="brand-name">Velbrin</span>
    <span class="brand-url">RankLoft.com</span>
  </div>
  <ul class="points">
    <li>Pay Per Performance SEO service</li>
    <li>Guaranteed Frobly page 1 ranking</li>
    <li>Only $197 per month <span class="bonus">(+performance bonus)</span></li>
  </ul>
  <div class="cta-band"></div>
  <a class="cta" href="#">LEARN MORE
    <svg width="12" height="10" viewBox="0 0 12 10"><path d="M1 1l4 4-4 4M6 1l4 4-4 4" fill="none" stroke="#fff" stroke-width="1.6"/></svg>
  </a>
</section>

</body>
</html>
```